FotoVELTA buisnesscard

Hey :) I need a modern buisnesscard for my company FotoVELTA
It most have:
Dagligleder og Fotograf: Henrik Torvald Bjelland

Mob: +4791642058
Epost: post@fotovelta.no
Adresse: Bakkestien22, 5412 Sjøvik

Facbook and instagram logo with text FotoVELTA

FotoVELTA logo

It Company

```html
<!DOCTYPE html>
<html lang="no">
<head>
<meta charset="utf-8">
<title>FotoVELTA – visittkort</title>
<link rel="stylesheet" href="https://fonts.googleapis.com/css2?family=Open+Sans:wght@400;600;700&display=swap">
<style>
  :root {
    --page-bg: #ececec;
    --card-white: #ffffff;
    --brand-blue: #2a7fb5;
    --brand-pink: #cc4a88;
    --text-grey: #4a4a4a;
    --divider: #c8c8c8;
  }
  * { margin: 0; padding: 0; box-sizing: border-box; }
  html, body {
    width: 1105px;
    height: 1200px;
    overflow: hidden;
    background: var(--page-bg);
    font-family: "Open Sans", Arial, sans-serif;
  }
  .canvas { position: relative; width: 1105px; height: 1200px; }

  .card {
    position: absolute;
    left: 193px;
    width: 720px;
    height: 410px;
    overflow: hidden;
  }
  .card--front { top: 167px; background: var(--card-white); }
  .card--back  { top: 623px; background: var(--brand-pink); }

  /* Front */
  .brand-name {
    position: absolute;
    left: 40px;
    width: 300px;
    top: 152px;
    text-align: center;
    font-size: 44px;
    font-weight: 700;
    color: var(--brand-blue);
    letter-spacing: -0.5px;
  }
  .divider {
    position: absolute;
    left: 359px;
    top: 91px;
    width: 1px;
    height: 195px;
    background: var(--divider);
  }
  .contact { position: absolute; left: 390px; top: 93px; }
  .contact__name {
    font-size: 25px;
    font-weight: 600;
    color: var(--brand-blue);
    line-height: 32px;
  }
  .contact__role {
    font-size: 19px;
    color: var(--brand-pink);
    line-height: 26px;
    margin-bottom: 12px;
  }
  .contact__address {
    font-size: 18px;
    color: var(--text-grey);
    line-height: 28px;
    margin-bottom: 10px;
  }
  .contact__line {
    display: flex;
    align-items: center;
    gap: 12px;
    font-size: 18px;
    color: var(--text-grey);
    line-height: 28px;
  }
  .contact__line svg { width: 18px; flex: none; }

  .footer-band {
    position: absolute;
    left: 0;
    top: 357px;
    height: 36px;
    width: 100%;
  }
  .footer-band__blue {
    position: absolute; left: 0; top: 0;
    width: 541px; height: 36px;
    background: var(--brand-blue);
  }
  .footer-band__pink {
    position: absolute; left: 589px; top: 0;
    right: 0; height: 36px;
    background: var(--brand-pink);
  }
  .website {
    position: absolute;
    left: 166px;
    top: 0;
    line-height: 36px;
    font-size: 18px;
    color: var(--card-white);
    letter-spacing: 3.5px;
  }

  /* Back */
  .back-brand {
    position: absolute;
    left: 0; right: 0;
    top: 165px;
    text-align: center;
    font-size: 66px;
    font-weight: 700;
    color: var(--card-white);
    letter-spacing: -1px;
  }
  .social-row { position: absolute; left: 0; top: 0; width: 720px; height: 410px; }
</style>
</head>
<body>
<div class="canvas">

  <section class="card card--front" aria-label="Visittkort forside">
    <div class="brand-name">FotoVELTA</div>
    <div class="divider"></div>

    <div class="contact">
      <div class="contact__name">Henrik Torvald Bjelland</div>
      <div class="contact__role">Dagligleder og Fotograf</div>
      <div class="contact__address">Bakkestien22<br>5412 Sjøvik</div>
      <div class="contact__line">
        <svg viewBox="0 0 18 24" aria-hidden="true">
          <rect x="3" y="1" width="12" height="22" rx="2" fill="none" stroke="var(--brand-blue)" stroke-width="2"/>
          <rect x="7" y="19" width="4" height="1.6" fill="var(--brand-blue)"/>
        </svg>
        <span>+4791642058</span>
      </div>
      <div class="contact__line">
        <svg viewBox="0 0 18 14" aria-hidden="true">
          <rect x="0" y="1" width="18" height="12" rx="1" fill="var(--brand-blue)"/>
          <path d="M1 2 L9 8 L17 2" fill="none" stroke="#fff" stroke-width="1.5"/>
        </svg>
        <span>post@fotovelta.no</span>
      </div>
    </div>

    <div class="footer-band">
      <div class="footer-band__blue"></div>
      <div class="footer-band__pink"></div>
      <div class="website">www.fotovelta.no</div>
    </div>
  </section>

  <section class="card card--back" aria-label="Visittkort bakside">
    <div class="back-brand">FotoVELTA</div>
    <svg class="social-row" viewBox="0 0 720 410" aria-hidden="true">
      <defs>
        <linearGradient id="fade-left" x1="0" x2="1">
          <stop offset="0" stop-color="#fff" stop-opacity="0"/>
          <stop offset="1" stop-color="#fff" stop-opacity="1"/>
        </linearGradient>
        <linearGradient id="fade-right" x1="0" x2="1">
          <stop offset="0" stop-color="#fff" stop-opacity="1"/>
          <stop offset="1" stop-color="#fff" stop-opacity="0"/>
        </linearGradient>
      </defs>
      <rect x="193" y="354" width="125" height="2" fill="url(#fade-left)"/>
      <rect x="403" y="354" width="125" height="2" fill="url(#fade-right)"/>
      <circle cx="340" cy="355" r="17" fill="none" stroke="#fff" stroke-width="2"/>
      <circle cx="381" cy="355" r="17" fill="none" stroke="#fff" stroke-width="2"/>
    </svg>
  </section>

</div>
</body>
</html>
```